Electrical company business card design.

Hi, were an electrical company in Auckland New Zealand called Quarneth Ltd. We focus mainly on high end residential and commercial so the card would be targeted towards that.
The card will be for myself, i am the director of the company.
Name: Derek Olstow
Position: Director/electrician
Phone: 021 387 9415
Email: derek@quarneth.co.nz
Location: Auckland
As for colors the the blue color in the logo is preferred, i also don't mind a black background option.
Target Market(s)
High end residential and commercial
Industry/Entity Type
Electrician
Contact Information for Business Card
Name: Derek Olstow Position: Director/Electrician Phone: 021 387 9415, Email: derek@quarneth.co.nz, Location: Auckland

```html
<!DOCTYPE html>
<html lang="en">
<head>
<meta charset="utf-8">
<title>Quarneth Ltd – Business Card</title>
<link href="https://fonts.googleapis.com/css2?family=Montserrat:wght@400;500;700&display=swap" rel="stylesheet">
<style>
  :root {
    --backdrop: #9a9a9a;
    --card-front: #ffffff;
    --card-back: #53585c;
    --brand-blue: #1457a8;
    --brand-grey: #54595d;
    --ink: #1f1f1f;
    --white: #ffffff;
  }
  * { margin: 0; padding: 0; box-sizing: border-box; }
  html, body {
    width: 1093px;
    height: 1200px;
    overflow: hidden;
    background: var(--backdrop);
    font-family: "Montserrat", sans-serif;
  }
  .canvas { position: relative; width: 1093px; height: 1200px; }

  .card {
    position: absolute;
    left: 265px;
    width: 595px;
    height: 362px;
    border-radius: 18px;
  }
  .card--front { top: 223px; background: var(--card-front); }
  .card--back  { top: 616px; height: 366px; background: var(--card-back); }

  .wordmark {
    position: absolute;
    display: flex;
    align-items: center;
    gap: 12px;
    font-weight: 500;
    letter-spacing: 1px;
    white-space: nowrap;
  }
  .wordmark__dot { width: 30px; height: 30px; border-radius: 50%; flex: none; }
  .card--front .wordmark { right: 46px; top: 56px; font-size: 44px; color: var(--brand-grey); }
  .card--front .wordmark__dot { background: var(--brand-blue); }
  .card--back .wordmark { left: 50%; top: 50%; transform: translate(-50%, -50%); font-size: 48px; color: var(--white); }
  .card--back .wordmark__dot { background: var(--white); width: 34px; height: 34px; }

  .person { position: absolute; left: 35px; top: 202px; }
  .person__name { font-size: 22px; font-weight: 700; color: var(--brand-blue); line-height: 1.1; }
  .person__role { font-size: 13.5px; color: var(--ink); margin-top: 3px; margin-left: 1px; }

  .divider {
    position: absolute;
    left: 36px; top: 253px;
    width: 533px; height: 1.5px;
    background: var(--brand-blue);
  }

  .contacts { position: absolute; left: 36px; top: 261px; list-style: none; }
  .contacts__item {
    display: flex; align-items: center; gap: 7px;
    height: 23px;
    font-size: 13.5px; color: var(--ink);
  }
  .contacts__icon { width: 14px; height: 14px; flex: none; fill: var(--brand-blue); }

  .location { position: absolute; right: 37px; top: 313px; font-size: 14px; color: var(--ink); }
</style>
</head>
<body>
<main class="canvas">
  <section class="card card--front" aria-label="Card front">
    <div class="wordmark"><span class="wordmark__dot"></span>QUARNETH</div>

    <div class="person">
      <h1 class="person__name">Derek Olstow</h1>
      <p class="person__role">Director/electrician</p>
    </div>

    <div class="divider"></div>

    <ul class="contacts">
      <li class="contacts__item">
        <svg class="contacts__icon" viewBox="0 0 24 24" aria-hidden="true"><path d="M6.6 10.8a15.1 15.1 0 0 0 6.6 6.6l2.2-2.2a1 1 0 0 1 1-.25 11.4 11.4 0 0 0 3.6.57 1 1 0 0 1 1 1V20a1 1 0 0 1-1 1A17 17 0 0 1 3 4a1 1 0 0 1 1-1h3.5a1 1 0 0 1 1 1c0 1.25.2 2.45.57 3.6a1 1 0 0 1-.25 1z"/></svg>
        021 387 9415
      </li>
      <li class="contacts__item">
        <svg class="contacts__icon" viewBox="0 0 24 24" aria-hidden="true"><path d="M2 5h20v2l-10 6L2 7z"/><path d="M2 9l10 6 10-6v10H2z"/></svg>
        derek@quarneth.co.nz
      </li>
      <li class="contacts__item">
        <svg class="contacts__icon" viewBox="0 0 24 24" aria-hidden="true"><circle cx="12" cy="12" r="10"/><path d="M7 6c2 1 1 3 3 4s1 3 0 4-1 3 0 5M15 4c-1 2 1 3 3 3M14 20c0-2 1-3 3-3s2-1 3-2" stroke="#fff" stroke-width="1.6" fill="none"/></svg>
        www.quarneth.co.nz
      </li>
    </ul>

    <p class="location">Auckland</p>
  </section>

  <section class="card card--back" aria-label="Card back">
    <div class="wordmark"><span class="wordmark__dot"></span>QUARNETH</div>
  </section>
</main>
</body>
</html>
```